Flyer design for Wander With Us Outback Trips

We need a new flyer for our tour business. Sketch horde produced a great flyer for us 4 years ago but it is time to update. We have had a price increase that needs to be reflected but we have noticed an issue with our current marketing.
Our tour is a "tagalong" tour which means you follow in your own vehicle. Unfortunately most people associate "tagalong" with 4wd (Four wheel drive vehicles). This is not the case for our tour which can be done in ANY type of vehicle. We need to get across at first glance that this tour is available to all vehicle types. We also need to stress that there is NOT MUCH DRIVING. We cover around 20km total of very easy driving. We go from point of interest to point of interest.
We want our customers to feel that this tour will be a better option than selecting a bus type tour because they use their own vehicle. Our option is also MUCH cheaper than bus options but provides a premium product. It's "cheap" but not cheap if you understand.
I will upload our previous flyer so you have an idea of what we do and how we have been presenting it. We are currently single sided DL but do not mind if we go into double sided DL if you feel that will enable you to share more information. Our price is $50 and half price for kids (as per old flyer)
Some things to remember when trying to appeal to our customer:
Choose a design that clearly communicates that our tagalong tour is suitable for all types of vehicles. For example, "Vehicle-Friendly Tagalong Tour" or "All-Vehicle Tagalong Tour".
Use clear language: Avoid using terms like "off-road" or "4x4" that may imply that our tour is only suitable for certain types of vehicles. Instead, use language that is inclusive and clearly communicates that all vehicles are welcome.
Include photos and videos of a variety of vehicles: This will show potential customers that our tagalong tour is not limited to four-wheel drive vehicles and that any type of vehicle can participate.
Highlight the benefits of a tagalong tour over a bus tour: Emphasise the flexibility and freedom that a tagalong tour offers, as well as the opportunity to explore off-the-beaten-path destinations that are not accessible by bus.
By incorporating these elements into your product presentation, you can avoid confusion and clearly communicate that our tagalong tour is suitable for any type of vehicle, while also highlighting the unique benefits of this type of tour.
Along with the emphasis on all vehicles you need to be clear about what we offer on the tour.
- The excitement of an opal mine tour with an award winning guide and opal miner.
- The wonder of an underground home and discovering how people live in an underground environment.
- Driving through the opal mining area for a close up view of the field.
- Our EXCLUSIVE opal cutting and polishing demonstration.
- The adventure of looking for your own opal.
For further information visit our web site "http://wanderwithus.outback.example". Check our facebook page "https://www.facebook.com/wanderwithusoutbacktrips". Search Seekr for "Coober Pedy", Wander with us Coober Pedy" or "Coober Pedy Opal mining" to source images of our town and opals.
PLEASE ALSO FIND SOMEWHERE TO SAY "FREE UNPOWERED CAMPING AT TOLMA'S WITH ALL TOURS AS WELL AS DISCOUNTS ON POWERED CAMPING" and make this stand out somehow. (http://rest-belowground.example.au)

Target Market(s)

18 to 80

Industry/Entity Type

Tourism

Font styles to use
Serif

Colors

Designer to choose colors to be used in the design.

Requirements
Must have
• Eye catching images and attention grabbing headlines
Nice to have
• Modern design.
Should not have
• References to 4wd or buses.

```html
<!DOCTYPE html>
<html lang="en">
<head>
<meta charset="utf-8">
<title>Wander With Us Outback Trips – Tagalong Tour Flyer</title>
<link rel="stylesheet" href="https://fonts.googleapis.com/css2?family=Anton&family=Poppins:wght@400;500;600;700;800&display=swap">
<style>
  :root {
    --orange: #f7890f;
    --orange-light: #ffab2e;
    --blue: #2a5f9e;
    --ink: #111111;
    --white: #ffffff;
    --paper: #ebebeb;
    --charcoal: #2b2b2b;
  }
  * { box-sizing: border-box; margin: 0; padding: 0; }
  html, body { width: 1200px; height: 2200px; overflow: hidden; }
  body { background: var(--paper); font-family: "Poppins", sans-serif; color: var(--ink); position: relative; }

  .flyer {
    position: absolute; top: 498px; width: 565px; height: 1204px;
    overflow: hidden; background: var(--white);
    box-shadow: 0 6px 18px rgba(0,0,0,.18);
  }
  .flyer--front { left: 25px; }
  .flyer--back { left: 610px; }
  .flyer__bg { position: absolute; inset: 0; width: 565px; height: 1204px; }
  .abs { position: absolute; }
  .center-x { left: 0; right: 0; text-align: center; }

  /* Front */
  .front__title {
    top: 42px; font-family: "Anton", sans-serif; font-size: 132px; line-height: 1;
    letter-spacing: -1px;
    background: linear-gradient(180deg, var(--orange-light), var(--orange) 70%, #e06d00);
    -webkit-background-clip: text; background-clip: text; color: transparent;
  }
  .front__rule { top: 189px; left: 70px; width: 425px; height: 2px; background: rgba(255,255,255,.55); }
  .front__subtitle { top: 198px; color: var(--white); font-weight: 800; font-size: 40px; line-height: 41px; }

  .price-badge {
    left: 48px; top: 519px; width: 224px; height: 224px; border-radius: 50%;
    background: var(--charcoal); border: 6px solid var(--ink);
    box-shadow: 0 0 0 3px var(--white) inset;
    color: var(--white); text-align: center; padding-top: 48px;
  }
  .price-badge__lead { font-size: 19px; font-weight: 400; }
  .price-badge__amount { display: flex; justify-content: center; align-items: center; gap: 4px; margin-top: -2px; }
  .price-badge__num { font-family: "Anton", sans-serif; font-size: 52px; color: var(--orange); line-height: 1; }
  .price-badge__per { font-size: 20px; line-height: 20px; text-align: left; }
  .price-badge__per b { font-weight: 700; }
  .price-badge__kids { font-size: 17px; line-height: 22px; margin-top: 6px; }
  .price-badge__kids b { font-weight: 700; }

  .brand-disc {
    width: 176px; height: 176px; border-radius: 50%; background: var(--orange);
    border: 5px solid var(--white); display: flex; align-items: center; justify-content: center;
    color: var(--white); font-weight: 600; font-size: 22px; line-height: 26px; text-align: center;
  }
  .front .brand-disc { left: 383px; top: 575px; }

  .pill-heading {
    top: 715px; left: 72px; width: 420px; height: 53px; border-radius: 27px;
    background: var(--ink); color: var(--white); font-weight: 800; font-size: 33px;
    text-align: center; line-height: 53px;
  }
  .front__driving { top: 778px; font-weight: 700; font-size: 21px; line-height: 27px; }

  .welcome-box {
    left: 43px; top: 866px; width: 481px; height: 140px; border: 2px solid var(--ink); border-radius: 18px;
  }
  .welcome-box__head {
    top: 838px; font-weight: 800; font-size: 36px; line-height: 40px;
  }
  .welcome-box__head span { background: var(--white); padding: 0 12px; }
  .welcome-box__accent { top: 878px; font-weight: 800; font-size: 46px; line-height: 50px; color: var(--orange); }
  .welcome-box__note { top: 944px; font-size: 15.5px; line-height: 20px; }

  /* Shared footer */
  .web-lead { top: 1026px; font-weight: 600; font-size: 17.5px; }
  .web-pill {
    top: 1055px; left: 61px; width: 442px; height: 42px; border-radius: 21px;
    background: var(--orange); color: var(--white); font-size: 22px; font-weight: 500;
    text-align: center; line-height: 42px;
  }
  .social { color: var(--white); font-size: 18px; font-weight: 500; }
  .social--page { top: 1110px; display: flex; justify-content: center; align-items: center; gap: 7px; }
  .social__square { width: 15px; height: 15px; background: var(--white); border-radius: 2px; display: inline-block; }
  .social--search { top: 1139px; letter-spacing: 1px; }
  .social--search .sep { color: var(--orange); margin: 0 5px; }
  .social--search em { font-style: normal; color: var(--orange); }

  /* Back */
  .back__title { top: 70px; color: var(--orange); font-weight: 800; font-size: 34px; }
  .back__intro { top: 115px; left: 60px; right: 60px; color: var(--white); font-weight: 700; font-size: 15.5px; line-height: 19px; text-align: center; }
  .back .brand-disc { left: 203px; top: 219px; width: 150px; height: 150px; font-size: 20px; line-height: 24px; }
  .back__offer { top: 385px; left: 57px; font-weight: 800; font-size: 29px; }
  .back__offer em { font-style: normal; color: var(--orange); }

  .offer-list { top: 438px; left: 59px; width: 460px; list-style: none; }
  .offer-item { display: flex; gap: 19px; align-items: flex-start; position: absolute; left: 0; width: 460px; }
  .offer-item__icon {
    flex: 0 0 44px; height: 44px; border-radius: 9px; background: var(--ink);
    display: flex; align-items: center; justify-content: center; margin-top: 8px;
  }
  .offer-item__icon--orange { background: var(--orange); }
  .offer-item__title { color: var(--orange); font-weight: 700; font-size: 15px; line-height: 19px; }
  .offer-item__text { font-size: 16.5px; line-height: 20px; }

  .camp-box { left: 43px; top: 843px; width: 481px; height: 135px; border: 2px solid var(--ink); border-radius: 18px; }
  .camp-free {
    top: 808px; left: 97px; background: var(--white); padding: 0 10px;
    font-family: "Anton", sans-serif; color: var(--orange); font-size: 76px; line-height: 84px;
  }
  .camp-kind { top: 818px; left: 243px; font-weight: 800; font-size: 30px; line-height: 34px; background: var(--white); padding-right: 8px; }
  .camp-kind__big { font-size: 38px; }
  .camp-detail { top: 898px; font-weight: 700; font-size: 18.5px; line-height: 26px; }
  .camp-pill {
    top: 959px; left: 98px; width: 370px; height: 42px; border-radius: 21px; background: var(--ink);
    color: var(--white); font-weight: 700; font-size: 17px; text-align: center; line-height: 42px;
  }
</style>
</head>
<body>

<!-- Front side -->
<section class="flyer flyer--front front" aria-label="Flyer front">
  <svg class="flyer__bg" viewBox="0 0 565 1204" aria-hidden="false">
    <defs>
      <linearGradient id="carsGrad" x1="0" y1="0" x2="0" y2="1">
        <stop offset="0" stop-color="#b9cfe6"/>
        <stop offset=".35" stop-color="#8a8f93"/>
        <stop offset=".6" stop-color="#a88a6c"/>
        <stop offset="1" stop-color="#c09a72"/>
      </linearGradient>
    </defs>
    <rect width="565" height="300" fill="#2a5f9e"/>
    <rect y="292" width="565" height="440" fill="url(#carsGrad)" role="img" aria-label="Photo of a line of sedans, wagons and utes parked on red dirt in an outback town, with tour guests gathered beside them"/>
    <path d="M0 700 C 140 690 330 700 565 790 L565 1204 L0 1204 Z" fill="#ffffff"/>
    <path d="M0 690 C 170 662 360 650 565 735 L565 790 C 380 700 190 690 0 708 Z" fill="#f7890f"/>
    <path d="M0 660 C 120 640 240 640 330 650 C 230 652 110 662 0 678 Z" fill="#f7890f"/>
    <rect y="1072" width="565" height="132" fill="#000"/>
  </svg>

  <div class="abs center-x front__title">tagalong</div>
  <div class="abs front__rule"></div>
  <h1 class="abs center-x front__subtitle">VEHICLE FRIENDLY<br>TAGALONG TOUR</h1>

  <div class="abs price-badge">
    <div class="price-badge__lead">Our price is</div>
    <div class="price-badge__amount">
      <span class="price-badge__num">$50</span>
      <span class="price-badge__per">PER<br><b>PERSON</b></span>
    </div>
    <div class="price-badge__kids">AND <b>HALF PRICE<br>FOR KIDS</b></div>
  </div>

  <div class="abs brand-disc">Wander<br>With Us</div>

  <h2 class="abs pill-heading">NOT MUCH DRIVING</h2>
  <p class="abs center-x front__driving">We cover around 20km total of<br>very easy driving.</p>

  <div class="abs welcome-box"></div>
  <h2 class="abs center-x welcome-box__head"><span>ALL VEHICLES</span></h2>
  <div class="abs center-x welcome-box__accent">ARE WELCOME</div>
  <p class="abs center-x welcome-box__note">Tagalong tour is not limited to four-wheel drive vehicles<br>and that any type of vehicle can participate.</p>

  <p class="abs center-x web-lead">For further information visit our web site</p>
  <div class="abs web-pill">www.wanderwithus.outback.example</div>
  <p class="abs center-x social social--page"><span class="social__square"></span>@wanderwithusoutbacktrips</p>
  <p class="abs center-x social social--search">Seekr<span class="sep">|</span>Wander with us <em>Coober Pedy</em></p>
</section>

<!-- Back side -->
<section class="flyer flyer--back back" aria-label="Flyer back">
  <svg class="flyer__bg" viewBox="0 0 565 1204">
    <defs>
      <linearGradient id="monoGrad" x1="0" y1="0" x2="1" y2="1">
        <stop offset="0" stop-color="#3a3a3a"/>
        <stop offset=".5" stop-color="#6b6b6b"/>
        <stop offset="1" stop-color="#2a2a2a"/>
      </linearGradient>
      <linearGradient id="convoyGrad" x1="0" y1="0" x2="0" y2="1">
        <stop offset="0" stop-color="#4d82c4"/>
        <stop offset=".45" stop-color="#a9c3de"/>
        <stop offset=".55" stop-color="#8b6b55"/>
        <stop offset="1" stop-color="#b9724a"/>
      </linearGradient>
    </defs>
    <rect width="565" height="520" fill="url(#monoGrad)" role="img" aria-label="Black and white photo of a vehicle parked on a rocky opal field"/>
    <path d="M0 385 C 180 300 380 330 565 500 L565 1204 L0 1204 Z" fill="#ffffff"/>
    <path d="M0 350 C 160 275 400 290 565 445 L565 510 C 400 350 170 320 0 395 Z" fill="#f7890f"/>
    <circle cx="150" cy="278" r="101" fill="#ffffff"/>
    <circle cx="150" cy="278" r="96" fill="url(#convoyGrad)" role="img" aria-label="Photo of a convoy of cars driving along a red dirt road under blue sky"/>
    <rect y="1072" width="565" height="132" fill="#000"/>
  </svg>

  <h1 class="abs center-x back__title">TAGALONG TOUR OFFERS</h1>
  <p class="abs back__intro">Flexibility and freedom , as well as the opportunity to explore off-the-beaten-path destinations that are not accessible by bus.</p>

  <div class="abs brand-disc">Wander<br>With Us</div>

  <h2 class="abs back__offer"><em>WE OFFER</em> ON THE TOUR</h2>

  <ul class="abs offer-list">
    <li class="offer-item" style="top:0">
      <span class="offer-item__icon"><svg width="24" height="24" viewBox="0 0 24 24"><circle cx="12" cy="7" r="3.5" fill="#fff"/><path d="M5 21 C5 14 19 14 19 21 Z" fill="#fff"/></svg></span>
      <div><div class="offer-item__title">THE EXCITEMENT</div><div class="offer-item__text">Of an opal mine tour with an award winning guide and opal miner.</div></div>
    </li>
    <li class="offer-item" style="top:79px">
      <span class="offer-item__icon offer-item__icon--orange"><svg width="24" height="24" viewBox="0 0 24 24"><circle cx="12" cy="12" r="8" fill="none" stroke="#fff" stroke-width="2"/><circle cx="9" cy="10" r="1.2" fill="#fff"/><circle cx="15" cy="10" r="1.2" fill="#fff"/><path d="M8.5 14.5 Q12 17.5 15.5 14.5" fill="none" stroke="#fff" stroke-width="1.6"/></svg></span>
      <div><div class="offer-item__title">THE WONDER</div><div class="offer-item__text">Of an underground home and discovering how people live in an underground environment.</div></div>
    </li>
    <li class="offer-item" style="top:154px">
      <span class="offer-item__icon"><svg width="24" height="24" viewBox="0 0 24 24"><rect x="4" y="8" width="16" height="8" rx="2" fill="#fff"/><circle cx="8" cy="17.5" r="2" fill="#fff"/><circle cx="16" cy="17.5" r="2" fill="#fff"/><rect x="7" y="5" width="10" height="4" rx="1" fill="#fff"/></svg></span>
      <div><div class="offer-item__title">DRIVING THROUGH</div><div class="offer-item__text">The opal mining area for a close up view of the field.</div></div>
    </li>
    <li class="offer-item" style="top:232px">
      <span class="offer-item__icon offer-item__icon--orange"><svg width="24" height="24" viewBox="0 0 24 24"><path d="M12 3 L14.6 9 L21 9.5 L16 13.6 L17.6 20 L12 16.5 L6.4 20 L8 13.6 L3 9.5 L9.4 9 Z" fill="none" stroke="#fff" stroke-width="1.6"/></svg></span>
      <div><div class="offer-item__title">OUR EXCLUSIVE</div><div class="offer-item__text">Opal cutting and polishing demonstration.</div></div>
    </li>
    <li class="offer-item" style="top:295px">
      <span class="offer-item__icon"><svg width="24" height="24" viewBox="0 0 24 24"><circle cx="10.5" cy="10.5" r="5.5" fill="none" stroke="#fff" stroke-width="2"/><path d="M14.5 14.5 L20 20" stroke="#fff" stroke-width="2.4" stroke-linecap="round"/></svg></span>
      <div><div class="offer-item__title">THE ADVENTURE</div><div class="offer-item__text">Of looking for your own opal.</div></div>
    </li>
  </ul>

  <div class="abs camp-box"></div>
  <div class="abs camp-free">FREE</div>
  <div class="abs camp-kind">UNPOWERED<br><span class="camp-kind__big">CAMPING</span></div>
  <p class="abs center-x camp-detail">AT TOLMA'S WITH ALL TOURS AS WELL AS<br>DISCOUNTS ON POWERED CAMPING</p>
  <div class="abs camp-pill">www.rest-belowground.example.au</div>

  <p class="abs center-x web-lead">For further information visit our web site</p>
  <div class="abs web-pill">www.wanderwithus.outback.example</div>
  <p class="abs center-x social social--page"><span class="social__square"></span>@wanderwithusoutbacktrips</p>
  <p class="abs center-x social social--search">Seekr<span class="sep">|</span>Wander with us <em>Coober Pedy</em></p>
</section>

</body>
</html>
```